business card for author of crime novel

I am an author with a new book. I need a business card with the book's cover on one side (already uploaded), and contact details on the other.

Walt Pemberty
Author

telephone: 646-512-7380
website: www.waltpemberty.net
facebook: facebook.com/wpemberty
twitter: twitter.com/wpemberty
email: wpemberty@postvale.net

Target Market(s)

Readers of mystery books

Industry/Entity Type

Business

Contact Information for Business Card

Walt Pemberty
Author

telephone: 646-512-7380

Font styles to use
Serif
Sans Serif

Requirements
Must have
• Book cover on one side. My contact info on the other, with the name of the book repeated if that makes sense. Clean design.
Should not have
• Overly ornate, too formal, too distracting

```html
<!DOCTYPE html>
<html lang="en">
<head>
<meta charset="utf-8">
<title>Walt Pemberty – Business Card</title>
<link rel="stylesheet" href="https://fonts.googleapis.com/css2?family=Cinzel:wght@400;500&family=Crimson+Text:wght@400&family=Old+Standard+TT:wght@700&display=swap">
<style>
  :root {
    --page-bg: #d9d9db;
    --card-white: #ffffff;
    --gold: #c9902e;
    --gold-text: #c28a2a;
    --ink: #1a1a1a;
    --muted: #9a9a9a;
    --rule: #b9b9b9;
    --band-grey: #b2b2b5;
    --cover-slate: #4b6673;
    --cover-steel: #8da3ad;
  }
  * { margin: 0; padding: 0; box-sizing: border-box; }
  html, body { width: 1200px; height: 1000px; overflow: hidden; }
  body {
    background: var(--page-bg);
    position: relative;
  }
  .card {
    position: absolute;
    left: 305px;
    width: 590px;
    height: 346px;
    background: var(--card-white);
    box-shadow: 0 4px 14px rgba(0,0,0,0.18);
    overflow: hidden;
  }
  .card--front { top: 100px; }
  .card--back { top: 520px; }

  /* Front: contact side */
  .identity {
    position: absolute;
    right: 156px;
    top: 44px;
    text-align: right;
  }
  .identity__name {
    font-family: "Cinzel", serif;
    font-weight: 500;
    font-size: 29px;
    color: var(--gold-text);
    letter-spacing: 0.5px;
    line-height: 1.1;
  }
  .identity__role {
    font-family: "Cinzel", serif;
    font-size: 16px;
    color: var(--muted);
    line-height: 1;
    margin-top: -2px;
  }
  .contact-list {
    position: absolute;
    left: 0;
    top: 160px;
    width: 436px;
    list-style: none;
    font-family: "Crimson Text", serif;
    font-size: 15.5px;
    color: var(--ink);
  }
  .contact-list li {
    height: 27.5px;
    line-height: 27.5px;
    text-align: right;
    white-space: nowrap;
    border-bottom: 1.5px solid var(--rule);
  }
  .contact-list li.contact-list__phone { height: 26px; }

  .title-band {
    position: absolute;
    top: 0;
    right: 0;
    width: 104px;
    height: 100%;
    background: var(--gold);
  }
  .title-band__text {
    position: absolute;
    left: 50%;
    top: 50%;
    width: 320px;
    transform: translate(-50%, -50%) rotate(-90deg);
    text-align: center;
  }
  .book-title {
    font-family: "Old Standard TT", serif;
    font-weight: 700;
    font-size: 31px;
    letter-spacing: 1.5px;
    color: var(--ink);
    line-height: 1.05;
    white-space: nowrap;
  }
  .book-series {
    font-family: "Crimson Text", serif;
    font-size: 16px;
    color: var(--ink);
    line-height: 1.2;
    white-space: nowrap;
  }

  /* Back: cover side */
  .side-band {
    position: absolute;
    top: 0;
    width: 56px;
    height: 100%;
    background: var(--band-grey);
  }
  .side-band--left { left: 0; }
  .side-band--right { right: 0; }
  .book-cover {
    position: absolute;
    left: 100px;
    top: 30px;
    width: 390px;
    height: 290px;
    background:
      radial-gradient(ellipse 60% 55% at 55% 42%, var(--cover-steel) 0%, var(--cover-slate) 70%, rgba(75,102,115,0) 100%),
      var(--gold);
    border-radius: 3px;
  }
</style>
</head>
<body>
  <section class="card card--front" aria-label="Card front: contact details">
    <div class="identity">
      <p class="identity__name">Walt Pemberty</p>
      <p class="identity__role">Author</p>
    </div>
    <ul class="contact-list">
      <li class="contact-list__phone">646-512-7380</li>
      <li>www.waltpemberty.net</li>
      <li>friendloop.com/wpemberty</li>
      <li>chirpline.com/wpemberty</li>
      <li>wpemberty@postvale.net</li>
    </ul>
    <div class="title-band">
      <div class="title-band__text">
        <p class="book-title">DEAD AIR ALLEY</p>
        <p class="book-series">A Hollis Grant Mystery</p>
      </div>
    </div>
  </section>

  <section class="card card--back" aria-label="Card back: book cover">
    <div class="side-band side-band--left"></div>
    <div class="side-band side-band--right"></div>
    <div class="book-cover" role="img" aria-label="Book cover of Dead Air Alley: gold paperback with a blue-toned photo of an old city building"></div>
  </section>
</body>
</html>
```